Vexolink Ad Image for Ebook

I need someone to design a good looking vexolink ad image for my ebook. Must comply with Vexolink ad police and generate lots of clicks and opt ins. Use my 3d cover attached.

```html
<!DOCTYPE html>
<html lang="en">
<head>
<meta charset="utf-8">
<title>Clever Writing Playbook – Ad</title>
<link href="https://fonts.googleapis.com/css2?family=Bebas+Neue&family=Montserrat:wght@300;600&display=swap" rel="stylesheet">
<style>
  :root {
    --stage: #bdb9b9;
    --blue: #1e8fd1;
    --blue-deep: #0a62a6;
    --accent-blue: #2a9be0;
    --red: #d7261e;
    --orange: #f06a2c;
    --black: #0b0b0b;
    --white: #ffffff;
    --photo: #dcdfe2;
  }
  * { margin: 0; padding: 0; box-sizing: border-box; }
  html, body { width: 1200px; height: 760px; overflow: hidden; }
  body { background: var(--stage); position: relative; font-family: "Bebas Neue", sans-serif; }

  .ad {
    position: absolute; left: 0; top: 68px; width: 1200px; height: 624px; overflow: hidden;
    background: linear-gradient(100deg, var(--blue) 0%, var(--blue) 55%, var(--blue-deep) 100%);
  }
  .ad__swoosh { position: absolute; inset: 0; }

  .hero-art {
    position: absolute; left: 190px; top: 110px; width: 300px; height: 310px;
    background: radial-gradient(ellipse at 50% 95%, rgba(255,255,255,.55) 0%, rgba(120,200,250,.35) 35%, rgba(30,143,209,0) 70%);
  }

  .sparkle { position: absolute; width: 26px; height: 26px; }

  .speech {
    position: absolute; left: 506px; top: 95px; width: 220px; height: 124px;
    background: var(--white); border-radius: 38px;
    display: flex; flex-direction: column; align-items: center; justify-content: center;
    font-size: 38px; line-height: .95; color: var(--black); letter-spacing: 1px;
  }
  .speech::after {
    content: ""; position: absolute; right: -22px; top: 2px;
    border-left: 40px solid var(--white); border-bottom: 36px solid transparent;
    transform: skewY(-20deg);
  }
  .speech__em { color: var(--red); }

  .cta {
    position: absolute; left: 60px; top: 422px; width: 544px; height: 116px;
    background: linear-gradient(180deg, #2a2a2a 0%, var(--black) 45%); border-radius: 14px;
    box-shadow: 0 2px 0 rgba(255,255,255,.15) inset;
    display: flex; align-items: center; justify-content: center;
    font-size: 56px; letter-spacing: 1px; color: var(--white); white-space: nowrap;
  }
  .cta__free { color: var(--orange); margin: 0 14px; }
  .cta__blueprint { color: var(--accent-blue); }

  .cursor { position: absolute; left: 429px; top: 527px; width: 58px; height: 88px; }

  .book {
    position: absolute; left: 767px; top: 27px; width: 327px; height: 575px;
    box-shadow: 14px 16px 30px rgba(0,0,0,.35);
  }
  .book__art { position: absolute; inset: 0; width: 100%; height: 100%; }
  .book__title {
    position: absolute; left: 24px; top: 380px;
    font-family: "Montserrat", sans-serif; font-weight: 300; font-size: 20px; line-height: 1.2;
    color: var(--white); text-transform: uppercase; white-space: nowrap;
  }
  .book__title strong { display: block; font-weight: 600; color: var(--accent-blue); font-size: 24px; }
  .book__brand {
    position: absolute; left: 170px; top: 492px; display: flex; align-items: center; gap: 8px;
    font-family: "Montserrat", sans-serif; font-weight: 600; font-size: 17px; color: var(--black);
    text-transform: uppercase; white-space: nowrap;
  }
  .book__brand-mark { width: 12px; height: 12px; background: var(--black); }
</style>
</head>
<body>
  <main class="ad">
    <svg class="ad__swoosh" viewBox="0 0 1200 624" preserveAspectRatio="none" aria-hidden="true">
      <path d="M0 0 H1200 V624 C1100 380 860 300 560 200 C360 130 200 40 0 0 Z" fill="rgba(255,255,255,.05)"/>
      <path d="M1200 300 C1130 420 1060 520 960 624 H1200 Z" fill="rgba(0,60,120,.25)"/>
    </svg>

    <div class="hero-art" role="img" aria-label="Illustration of a raised fist holding a red megaphone with light rays behind it"></div>

    <svg class="sparkle" style="left:188px;top:227px" viewBox="0 0 26 26" aria-hidden="true"><path d="M13 2v22M2 13h22" stroke="#fff" stroke-width="4" stroke-linecap="round"/></svg>
    <svg class="sparkle" style="left:469px;top:295px" viewBox="0 0 26 26" aria-hidden="true"><path d="M13 2v22M2 13h22" stroke="#fff" stroke-width="4" stroke-linecap="round"/></svg>
    <svg class="sparkle" style="left:236px;top:571px" viewBox="0 0 26 26" aria-hidden="true"><path d="M13 2v22M2 13h22" stroke="#fff" stroke-width="4" stroke-linecap="round"/></svg>

    <div class="speech">
      <span>Download it</span>
      <span class="speech__em">Now!</span>
    </div>

    <div class="cta">
      <span>Get this</span><span class="cta__free">Free</span><span class="cta__blueprint">Blueprint</span>
    </div>

    <svg class="cursor" viewBox="0 0 58 88" aria-hidden="true">
      <path d="M2 2 L2 70 L18 56 L30 84 L42 79 L30 52 L54 52 Z" fill="#fff" stroke="#c9d3dc" stroke-width="2" stroke-linejoin="round"/>
    </svg>

    <div class="book">
      <svg class="book__art" viewBox="0 0 327 575" preserveAspectRatio="none">
        <rect width="327" height="575" fill="var(--photo)" role="img" aria-label="Photo of a person typing on a laptop showing a blog page"/>
        <polygon points="0,312 226,355 124,575 0,575" fill="var(--black)"/>
        <polygon points="327,275 226,355 327,397" fill="var(--blue)"/>
        <polygon points="226,355 327,397 327,575 124,575" fill="var(--white)"/>
      </svg>
      <div class="book__title">The Clever<br>Writing<strong>Playbook</strong></div>
      <div class="book__brand"><span class="book__brand-mark"></span>Corin Media</div>
    </div>
  </main>
</body>
</html>
```